Varlowe Supply Partners
Business Cards and Stationary
Project: Varlowe Supply Partners
Varlowe Supply Partners -
Creative Brief
Professional
Daniel Varlowe
Manufacturer's Representative
20375 82nd Lane NW Elk Ridge, MN 55492
dvarlowe@varlowesupply-example.com
www.varlowesupply-example.com

```html
<!DOCTYPE html>
<html lang="en">
<head>
<meta charset="utf-8">
<title>Varlowe Supply Partners – Business Cards</title>
<link href="https://fonts.googleapis.com/css2?family=Italianno&family=Arimo:wght@400;700&display=swap" rel="stylesheet">
<style>
  :root {
    --backdrop: #5b5b5b;
    --card-white: #ffffff;
    --navy: #0c3f78;
    --sky: #1b8ad6;
    --label-blue: #1a4f8f;
    --text-grey: #4a4a4a;
  }
  html, body {
    margin: 0;
    width: 1200px;
    height: 901px;
    overflow: hidden;
    background: var(--backdrop);
    font-family: "Arimo", Arial, sans-serif;
  }
  .canvas { position: relative; width: 1200px; height: 901px; }

  .card { position: absolute; overflow: hidden; }

  /* Front card */
  .card-front {
    left: 34px; top: 34px; width: 652px; height: 406px;
    background: var(--card-white);
  }
  .card-front .waves { position: absolute; left: 0; top: 0; }
  .front-name {
    position: absolute; right: 34px; top: 48px; margin: 0;
    font-family: "Italianno", cursive;
    font-weight: 400; font-size: 50px; line-height: 1;
    color: var(--navy);
  }
  .front-title {
    position: absolute; right: 34px; top: 96px; margin: 0;
    font-size: 11.5px; letter-spacing: 0.3px;
    color: var(--sky); text-transform: uppercase;
  }
  .contact-list { position: absolute; left: 37px; top: 146px; margin: 0; }
  .contact-row { position: absolute; left: 0; display: flex; white-space: nowrap; }
  .contact-row dt {
    width: 97px; font-size: 11.5px; font-weight: 700;
    color: var(--label-blue); text-transform: uppercase;
  }
  .contact-row dd { margin: 0; font-size: 11px; line-height: 15px; color: var(--text-grey); }
  .contact-row dd.caps { text-transform: uppercase; }

  /* Back card */
  .card-back {
    left: 535px; top: 477px; width: 628px; height: 409px;
    background: var(--navy);
  }
  .back-name {
    position: absolute; left: 0; width: 100%; top: 150px; margin: 0;
    text-align: center;
    font-family: "Italianno", cursive;
    font-weight: 400; font-size: 104px; line-height: 1;
    color: var(--card-white);
  }
  .back-title {
    position: absolute; left: 240px; top: 243px; margin: 0;
    font-size: 11.5px; color: var(--sky); text-transform: uppercase;
  }
  .back-web {
    position: absolute; left: 0; width: 100%; top: 376px; margin: 0;
    text-align: center; font-size: 17px; color: var(--sky);
  }
</style>
</head>
<body>
<main class="canvas">

  <section class="card card-front" aria-label="Business card front">
    <svg class="waves" width="652" height="406" viewBox="0 0 652 406" aria-hidden="true">
      <path d="M0,312 C240,332 480,302 652,212 L652,406 L0,406 Z" fill="var(--sky)"/>
      <path d="M0,332 C240,338 480,320 652,245 L652,406 L0,406 Z" fill="var(--navy)"/>
    </svg>
    <h1 class="front-name">Daniel Varlowe</h1>
    <p class="front-title">Manufacturer's Representative</p>
    <dl class="contact-list">
      <div class="contact-row" style="top:0">
        <dt>Address</dt>
        <dd class="caps">20375 82nd Lane NW<br>Elk Ridge, MN 55492</dd>
      </div>
      <div class="contact-row" style="top:41px">
        <dt>Phone</dt><dd>763.555.0148</dd>
      </div>
      <div class="contact-row" style="top:69px">
        <dt>Fax</dt><dd>763.555.0172</dd>
      </div>
      <div class="contact-row" style="top:95px">
        <dt>Email</dt><dd>dvarlowe@varlowesupply-example.com</dd>
      </div>
      <div class="contact-row" style="top:122px">
        <dt>Web Address</dt><dd>www.varlowesupply-example.com</dd>
      </div>
    </dl>
  </section>

  <section class="card card-back" aria-label="Business card back">
    <h2 class="back-name">Daniel Varlowe</h2>
    <p class="back-title">Manufacturer's Representative</p>
    <p class="back-web">www.varlowesupply-example.com</p>
  </section>

</main>
</body>
</html>
```